Local Directory Ad

We currently have an advertisement in our local directory (see attached). We would like to make it look more appealing.
Dimensions are 110mm H X 175mm W
We would like to keep the same colours and contact details remain the same.
Most of the content can remain the same, Just remove the line Tax effective remote area salary packaging and add in Self Managed Super Funds.We want to change mortgage broking to Mortgage Broking and Loan Structuring.

We want to change the line Local accountants Local Knowledge Local Experience - to something like local knowledge beyond compare or unsurpassed local knowledge but open to suggestions on this.

there are some good designs posted so far. I particulalry like the ones from pulmawick, korbu41, and the last one posted by wexlorunti and PLV. Keep up the good work guys

```html
<!DOCTYPE html>
<html lang="en">
<head>
<meta charset="utf-8">
<title>Marlow Accounting &amp; Finance – Directory Ad</title>
<link href="https://fonts.googleapis.com/css2?family=Open+Sans:ital,wght@0,400;0,700;1,700;1,800&display=swap" rel="stylesheet">
<style>
  :root {
    --page: #ffffff;
    --red: #e4202a;
    --red-deep: #a8141b;
    --charcoal: #3a3532;
    --white: #ffffff;
    --ink: #3d3d3d;
    --ink-soft: #555555;
  }
  html, body {
    margin: 0;
    width: 1200px;
    height: 1200px;
    overflow: hidden;
    background: var(--page);
  }
  .ad {
    position: absolute;
    left: 139px;
    top: 311px;
    width: 922px;
    height: 578px;
    box-sizing: border-box;
    padding: 12px;
    border-radius: 62px;
    background: linear-gradient(90deg, var(--red-deep), var(--red) 25%, var(--red) 75%, var(--red-deep));
  }
  .ad__inner {
    position: relative;
    height: 100%;
    border-radius: 50px;
    overflow: hidden;
    background: var(--white);
    display: flex;
    flex-direction: column;
  }
  .masthead {
    height: 238px;
    flex: none;
    background: var(--charcoal);
    color: var(--white);
    text-align: center;
    display: flex;
    flex-direction: column;
    justify-content: center;
    font-family: "Open Sans", sans-serif;
  }
  .brand {
    margin: 0;
    font-weight: 700;
    font-size: 48px;
    line-height: 1.1;
    color: var(--white);
  }
  .tagline {
    margin: 18px 0 0;
    font-style: italic;
    font-weight: 700;
    font-size: 20px;
  }
  .services {
    height: 160px;
    flex: none;
    box-sizing: border-box;
    padding: 16px 0 0 68px;
    color: var(--white);
    font-family: "Open Sans", sans-serif;
    background: linear-gradient(90deg, var(--red-deep), var(--red) 22%, var(--red) 78%, var(--red-deep));
  }
  .services__lead {
    margin: 0 0 6px;
    font-style: italic;
    font-weight: 800;
    font-size: 23px;
  }
  .services__list {
    list-style: none;
    margin: 0;
    padding: 0;
    display: grid;
    grid-template-columns: 258px auto;
    row-gap: 1px;
    font-size: 21px;
    line-height: 1.28;
  }
  .services__list li::before {
    content: "";
    display: inline-block;
    width: 7px;
    height: 7px;
    border-radius: 50%;
    background: var(--white);
    margin: 0 7px 4px 0;
    vertical-align: middle;
  }
  .licence {
    position: absolute;
    right: 6px;
    top: 196px;
    writing-mode: vertical-rl;
    transform: rotate(180deg);
    white-space: nowrap;
    font-family: "Open Sans", sans-serif;
    font-size: 9.5px;
    color: var(--white);
    opacity: 0.85;
  }
  .contact {
    flex: 1;
    position: relative;
    font-family: "Open Sans", sans-serif;
    color: var(--ink-soft);
  }
  .contact__address {
    position: absolute;
    left: 45px;
    top: 20px;
    margin: 0;
    font-style: normal;
    font-size: 17.5px;
    line-height: 1.35;
  }
  .contact__direct {
    position: absolute;
    right: 50px;
    top: 64px;
    color: var(--ink);
  }
  .contact__phone {
    display: block;
    font-size: 34px;
    letter-spacing: 1px;
    line-height: 1.1;
  }
  .contact__web {
    display: block;
    font-size: 20px;
    color: var(--ink-soft);
  }
  .contact__web b { color: var(--ink); }
</style>
</head>
<body>
  <article class="ad">
    <div class="ad__inner">
      <header class="masthead">
        <h1 class="brand">Marlow Accounting &amp; Finance</h1>
        <p class="tagline">Local knowledge beyond compare or unsurpassed local knowledge</p>
      </header>

      <section class="services">
        <p class="services__lead">We are here for you all year round to assist with...</p>
        <ul class="services__list">
          <li>Accounting &amp; Taxation</li>
          <li>Business Advice</li>
          <li>GST and BAS’s</li>
          <li>Mortgage Broking and Loan Structuring</li>
          <li>Bookkeeping</li>
          <li>Self Managed Super Funds for your employees</li>
        </ul>
      </section>

      <span class="licence">Australian Credit Licence 412 608</span>

      <footer class="contact">
        <address class="contact__address">
          Shop 5 Quayside Arcade<br>
          12 Tarrant St Port Calder,<br>
          PO Box 418 Port Calder 6734<br>
          Email: reception@mwaf.com.au<br>
          Fax: 9458 2913
        </address>
        <div class="contact__direct">
          <span class="contact__phone">9184 3071</span>
          <span class="contact__web">www.<b>mwaf</b>.com.au</span>
        </div>
      </footer>
    </div>
  </article>
</body>
</html>
```